Stonelynk Business Card Design

The Stonelynk Co is an aggregate (crushing) equipment dealer serving Western Canadian provinces. Stonelynk is a distributor of aggregate equipment for different manufacturers.

We are looking to change and update the existing business card which has been used since the existence of the company. A copy of existing card has been attached for reference. The Stonelynk Co logo we want to remain the same and we want the green color to remain the same.

We are wanting something new with a different look. A refreshing card to show a new modern and updated look. No longer wanting to have the manufacturers on the back of the card but something more like our logo on the back of the card with a statement like "Crushing Solutions"

ideas could be:
- card can be different colors on front and back
- front or reverse of the card could possibly be the green color with the logo in black

Target Market(s)

Owners of Aggregate/Crushing companies

Requirements
Must have
• - logo to remain same along with same font within logo
• - green color to remain same
Nice to have
• as noted above under project description
Should not have

```html
<!DOCTYPE html>
<html lang="en">
<head>
<meta charset="utf-8">
<title>The Stonelynk Co. – Business Card</title>
<link rel="stylesheet" href="https://fonts.googleapis.com/css2?family=Archivo:wght@800&family=Raleway:wght@500&family=Open+Sans:wght@400&display=swap">
<style>
  :root {
    --olive: #8e8c35;
    --ink: #231f20;
    --paper: #ffffff;
    --backdrop: #dcdcdc;
  }
  html, body {
    margin: 0;
    width: 1200px;
    height: 1000px;
    overflow: hidden;
    background: var(--backdrop);
  }
  .canvas { position: relative; width: 1200px; height: 1000px; }
  .card {
    position: absolute;
    background: var(--paper);
    border-radius: 40px;
    overflow: hidden;
  }
  .card-front { left: 148px; top: 100px; width: 632px; height: 362px; }
  .card-back  { left: 370px; top: 545px; width: 637px; height: 363px; }
  .card svg.shapes { position: absolute; inset: 0; }

  .front-name {
    position: absolute; left: 0; right: 0; top: 212px;
    text-align: center;
    font: 800 33px/1 "Archivo", sans-serif;
    color: var(--ink);
    letter-spacing: 0.2px;
  }
  .front-tagline {
    position: absolute; left: 0; right: 0; top: 271px;
    text-align: center;
    font: 500 18px/1 "Raleway", sans-serif;
    color: var(--olive);
    letter-spacing: 0.5px;
  }

  .back-header {
    position: absolute; left: 0; top: 0; width: 100%; height: 130px;
    background: var(--olive);
  }
  .holder-name {
    position: absolute; left: 30px; top: 80px;
    font: 500 28px/1 "Raleway", sans-serif;
    color: var(--paper);
  }
  .company-name {
    position: absolute; left: 392px; top: 94px;
    font: 800 15px/1 "Archivo", sans-serif;
    color: var(--paper);
  }
  .address {
    position: absolute; left: 97px; top: 132px; width: 438px; height: 30px;
    display: flex; align-items: center; justify-content: center;
    font: 400 15px/1 "Open Sans", sans-serif;
    color: var(--paper);
  }
  .contact-list {
    position: absolute; margin: 0; padding: 0; list-style: none;
    font: 400 23px/1 "Open Sans", sans-serif;
    color: var(--ink);
  }
  .contact-list li { display: flex; align-items: center; height: 34px; }
  .contact-list svg { width: 20px; height: 20px; margin-right: 17px; fill: var(--ink); }
  .contact-phones { left: 28px; top: 182px; }
  .contact-online { left: 318px; top: 182px; }
  .back-footer {
    position: absolute; left: 0; bottom: 0; width: 100%; height: 68px;
    background: var(--ink);
    display: flex; align-items: center; justify-content: center;
    font: 400 20px/1 "Open Sans", sans-serif;
    color: var(--paper);
  }
  .back-footer span { padding: 0 12px; }
  .back-footer .divider { width: 2px; height: 28px; background: var(--paper); padding: 0; }
</style>
</head>
<body>
<div class="canvas">

  <section class="card card-front">
    <svg class="shapes" width="632" height="362" viewBox="0 0 632 362" aria-hidden="true">
      <path fill="var(--olive)" d="M0,43 C40,52 64,62 64,100 L64,252 C64,288 40,300 0,315 Z"/>
      <path fill="var(--olive)" d="M632,43 C592,55 566,66 566,100 L566,255 C566,290 590,300 632,317 Z"/>
    </svg>
    <div class="front-name">THE STONELYNK CO.</div>
    <div class="front-tagline">CRUSHING SOLUTIONS</div>
  </section>

  <section class="card card-back">
    <div class="back-header"></div>
    <svg class="shapes" width="637" height="363" viewBox="0 0 637 363" aria-hidden="true">
      <path fill="var(--ink)" d="M97,132 L535,132 C522,148 512,162 495,162 L132,162 C115,162 106,148 97,132 Z"/>
    </svg>
    <div class="holder-name">DALE MARWICK</div>
    <div class="company-name">THE STONELYNK CO.</div>
    <div class="address">2210-48B AVENUE, NISKU, ALBERTA T9E 3K1</div>

    <ul class="contact-list contact-phones">
      <li><svg viewBox="0 0 20 20"><path d="M1,7 C1,3 19,3 19,7 L19,9 L14,9 L14,7 L6,7 L6,9 L1,9 Z M5,10 L15,10 L18,17 L2,17 Z"/></svg>780 . 555 . 0142</li>
      <li><svg viewBox="0 0 20 20"><path d="M4,2 L8,2 L9,7 L6.5,8.5 C7.5,11 9,12.5 11.5,13.5 L13,11 L18,12 L18,16 C18,17 17,18 16,18 C9,18 2,11 2,4 C2,3 3,2 4,2 Z"/></svg>780 . 555 . 0187</li>
      <li><svg viewBox="0 0 20 20"><path d="M5,2 L13,2 L15,4 L15,7 L5,7 Z M2,8 L18,8 L18,15 L15,15 L15,18 L5,18 L5,15 L2,15 Z"/></svg>780 . 555 . 0163</li>
    </ul>
    <ul class="contact-list contact-online">
      <li><svg viewBox="0 0 20 20"><path d="M2,5 L18,5 L10,11 Z M2,7 L10,13 L18,7 L18,16 L2,16 Z"/></svg>dale@stonelynk.com</li>
      <li><svg viewBox="0 0 20 20"><path fill="none" stroke="var(--ink)" stroke-width="1.6" d="M10,2 A8,8 0 1 0 10.01,2 Z M2,10 L18,10 M10,2 C6,6 6,14 10,18 M10,2 C14,6 14,14 10,18"/></svg>www.stonelynk.ca</li>
    </ul>

    <div class="back-footer">
      <span>SCREENERS</span><span class="divider"></span><span>CRUSHERS</span><span class="divider"></span><span>STACKERS</span>
    </div>
  </section>

</div>
</body>
</html>
```